Fontaneau Bayou Grillhouse (Owners Card)

Need a classy, but modern business card. I have included a promotional card for the steakhouse. I need one for myself (the owner) that is more professional.

Target Market(s)

General Public

Industry/Entity Type

Food service

Contact Information for Business Card

Name, business address, phone number, email, logo

Font styles to use
Serif
Sans Serif
Decorative
Script

Requirements
Must have
• My name (Darvin Okafor), business address (627 Harlow Avenue), phone number (520) 394-2751, email (Dokaforzp4@mailbrook.net. On the back of the card: Psalms 27 1 The LORD is my light and my salvation— whom shall I fear? The LORD is the stronghold of my life— of whom shall I be afraid? 2 When the wicked advance against me to devour me, it is my enemies and my foes who will stumble and fall. 3 Though an army besiege me, my heart will not fear; though war break out against me, even then I will be confident.
Nice to have
• Something that’s bold, but modern and professional.

```html
<!DOCTYPE html>
<html lang="en">
<head>
<meta charset="utf-8">
<title>Fontaneau Bayou Grillhouse – Owner Card</title>
<link rel="stylesheet" href="https://fonts.googleapis.com/css2?family=Cinzel:wght@400;600&family=Arimo:wght@400;700&display=swap">
<style>
  :root {
    --stage: #3a3a3a;
    --card: #333333;
    --edge: #22d422;
    --brand-green: #1fb51f;
    --accent: #f05a0e;
    --ink: #f4f4f4;
    --rule: #bdbdbd;
  }
  * { margin: 0; padding: 0; box-sizing: border-box; }
  html, body { width: 1200px; height: 803px; overflow: hidden; }
  body {
    background: var(--stage);
    font-family: "Arimo", Arial, sans-serif;
    color: var(--ink);
    position: relative;
  }
  .card {
    position: absolute;
    top: 247px;
    width: 540px;
    height: 309px;
    background: var(--card);
    border-radius: 22px;
    border-bottom: 3px solid var(--edge);
    box-shadow: 0 18px 40px rgba(0,0,0,.45);
  }
  .card--front { left: 30px; }
  .card--back { left: 630px; }

  /* Front */
  .identity {
    position: absolute;
    left: 48px;
    top: 104px;
    width: 200px;
    text-align: right;
  }
  .identity__name {
    font-family: "Cinzel", "Times New Roman", serif;
    font-weight: 400;
    font-size: 27px;
    line-height: 1.1;
    color: var(--brand-green);
    letter-spacing: .5px;
  }
  .identity__role {
    margin-top: 4px;
    font-size: 14px;
    color: var(--ink);
  }
  .divider {
    position: absolute;
    left: 266px;
    top: 92px;
    width: 1px;
    height: 82px;
    background: var(--rule);
  }
  .contacts {
    position: absolute;
    left: 282px;
    top: 96px;
    list-style: none;
    font-size: 13.5px;
    line-height: 25px;
  }
  .contacts li { display: flex; align-items: center; gap: 8px; }
  .contacts svg { width: 13px; height: 13px; flex: none; }
  .address {
    position: absolute;
    left: 0;
    right: 0;
    top: 236px;
    text-align: center;
    font-size: 14px;
    letter-spacing: .3px;
  }

  /* Back */
  .brand {
    position: absolute;
    left: 0; right: 0;
    top: 34px;
    display: flex;
    flex-direction: column;
    align-items: center;
    gap: 10px;
  }
  .brand__mark {
    width: 34px; height: 34px;
    border-radius: 50%;
    background: var(--brand-green);
  }
  .brand__name {
    font-family: "Cinzel", "Times New Roman", serif;
    font-weight: 600;
    font-size: 21px;
    color: var(--brand-green);
    letter-spacing: .5px;
  }
  .verse {
    position: absolute;
    left: 0; right: 0;
    top: 128px;
    text-align: center;
  }
  .verse__title {
    font-weight: 700;
    font-size: 15px;
    color: var(--accent);
    letter-spacing: .6px;
    margin-bottom: 6px;
  }
  .verse__line {
    font-size: 12.5px;
    line-height: 18.5px;
  }
</style>
</head>
<body>
  <section class="card card--front" aria-label="Business card front">
    <div class="identity">
      <h1 class="identity__name">Darvin Okafor</h1>
      <p class="identity__role">Owner</p>
    </div>
    <div class="divider"></div>
    <ul class="contacts">
      <li>
        <svg viewBox="0 0 16 16" aria-hidden="true"><path fill="#f05a0e" d="M4 1l2.5 3-1.6 1.6a9 9 0 0 0 5.5 5.5L12 9.5l3 2.5-1.5 2.5C7.5 15 1 8.5 1.5 2.5z"/></svg>
        (520) 394-2751
      </li>
      <li>
        <svg viewBox="0 0 16 16" aria-hidden="true"><rect x="1" y="3" width="14" height="10" fill="#f05a0e"/><path d="M1 3l7 6 7-6" fill="none" stroke="#333" stroke-width="1.4"/></svg>
        Dokaforzp4@mailbrook.net
      </li>
      <li>
        <svg viewBox="0 0 16 16" aria-hidden="true"><circle cx="8" cy="8" r="7" fill="#f05a0e"/><path d="M1 8h14M8 1c-3 3-3 11 0 14M8 1c3 3 3 11 0 14" fill="none" stroke="#333" stroke-width="1.1"/></svg>
        Fontbayou.com
      </li>
    </ul>
    <p class="address">627 Harlow Avenue, Lakemont, CA 94871</p>
  </section>

  <section class="card card--back" aria-label="Business card back">
    <div class="brand">
      <span class="brand__mark"></span>
      <p class="brand__name">Fontaneau Bayou Grillhouse</p>
    </div>
    <div class="verse">
      <h2 class="verse__title">PSALMS 27</h2>
      <p class="verse__line">The LORD is my light and my salvation— whom shall I fear?</p>
      <p class="verse__line">The LORD is the stronghold of my life— of whom shall I be afraid?</p>
      <p class="verse__line">When the wicked advance against me to devour me,</p>
      <p class="verse__line">it is my enemies and my foes who will stumble and fall.</p>
      <p class="verse__line">Though an army besiege me, my heart will not fear;</p>
      <p class="verse__line">though war break out against me, even then I will be confident.</p>
    </div>
  </section>
</body>
</html>
```